Geschäftspapier für einen ambulanten Pflegedienst
Zielgruppe
Wir sind ein ambulanter Pflegedienst, der sich an pflegebedürftige Menschen jeden Alters richtet.
Aufgabenstellung
SorgeTaubeWerden
Gustav-Lindner-Weg 7
10612 Berlin
Varen Bank AG München
Konto 00 584 392 71
BLZ 700 518 00
IBAN DE47 7005 1800 0058 4392 7
BIC VRKADEMMXXX
Sitz der Gesellschaft: Berlin, Deutschland
Geschäftsführung: Henrik Bosselt
Handelsregister: AG Berlin
HRB 258913
SteuerID 31/862/41597
IK Nummer 537 648 219
Tel. 030 714 263 591
Fax. 030 714 263 592
eMail: info@sorgetaubewerden.example
www.sorgetaubewerden.example

```html
<!DOCTYPE html>
<html lang="de">
<head>
<meta charset="utf-8">
<title>SorgeTaubeWerden – Briefbogen</title>
<link href="https://fonts.googleapis.com/css2?family=Arimo:wght@400&family=Open+Sans:wght@400;600;700&display=swap" rel="stylesheet">
<style>
  :root{
    --bg:#ececed;
    --paper:#ffffff;
    --accent:#d9502f;
    --grey:#8a8c8f;
    --ink:#2b2b2b;
    --muted:#4a4a4a;
    --faint:#f1f1f1;
  }
  *{margin:0;padding:0;box-sizing:border-box}
  html,body{width:1200px;height:1010px;overflow:hidden;background:var(--bg)}
  .sheet{
    position:absolute;left:260px;top:24px;width:680px;height:962px;
    background:var(--paper);box-shadow:0 2px 14px rgba(0,0,0,.12);
    overflow:hidden;font-family:"Open Sans",Arial,sans-serif;color:var(--ink);
  }
  .brand{position:absolute;right:62px;top:58px;display:flex;align-items:center;gap:8px}
  .brand-mark{width:14px;height:14px;background:var(--accent)}
  .brand-name{font-weight:700;font-size:24px;color:var(--accent);letter-spacing:.2px}
  .contact{
    position:absolute;left:462px;top:112px;padding-left:12px;
    border-left:1px solid var(--grey);font-size:9.5px;line-height:14px;color:var(--ink)
  }
  .contact .firm{font-weight:600}
  .contact .row{display:flex;align-items:center;gap:6px}
  .contact svg{width:9px;height:9px;fill:var(--accent);flex:none}
  .return-line{
    position:absolute;left:74px;top:232px;font-size:7.5px;color:var(--muted);
    border-bottom:1px solid var(--grey);padding-bottom:2px
  }
  .return-line .sep{color:var(--accent);margin:0 3px}
  .fold-mark{position:absolute;left:0;width:18px;height:1px;background:var(--grey)}
  .fold-mark.top{top:320px}
  .fold-mark.punch{top:481px}
  .letter{
    position:absolute;left:74px;top:318px;width:470px;
    font-family:"Arimo",Arial,sans-serif;font-size:11.5px;line-height:15px;color:var(--ink)
  }
  .letter .salutation{margin-bottom:12px}
  .letter p{margin-bottom:14px}
  .signature{width:150px;height:46px;margin-top:10px;background:linear-gradient(90deg,#f4f4f4,#e9e9e9);border-radius:3px}
  .watermark{
    position:absolute;right:40px;top:650px;font-weight:700;font-size:58px;
    color:var(--faint);letter-spacing:.5px;pointer-events:none
  }
  .footer-info{
    position:absolute;left:74px;right:40px;bottom:52px;display:flex;gap:14px;
    font-size:9px;line-height:12.5px;color:var(--ink)
  }
  .footer-info .col{padding-left:10px;border-left:1px solid var(--accent)}
  .footer-info .col:first-child{padding-left:0;border-left:none}
  .footer-rule{position:absolute;left:0;right:190px;bottom:16px;height:3px;background:var(--grey)}
  .footer-band{position:absolute;left:0;right:0;bottom:0;height:12px;background:var(--accent)}
  .web-tab{
    position:absolute;right:0;bottom:0;width:196px;height:34px;background:var(--accent);
    border-top-left-radius:14px;color:#fff;font-size:10.5px;
    display:flex;align-items:center;justify-content:center;padding-bottom:6px
  }
</style>
</head>
<body>
  <main class="sheet">
    <header>
      <div class="brand">
        <span class="brand-mark"></span>
        <span class="brand-name">SorgeTaubeWerden</span>
      </div>
      <address class="contact">
        <div class="firm">SorgeTaubeWerden</div>
        <div>Gustav-Lindner-Weg 7</div>
        <div>10612 Berlin</div>
        <div class="row"><svg viewBox="0 0 10 10"><path d="M2 0.5l2 2-1 1.2c.6 1.3 1.6 2.3 2.9 2.9L7.1 5.6l2.4 2-1.2 1.9C4.5 9.5.5 5.5.5 1.7z"/></svg>030 714 263 591</div>
        <div class="row"><svg viewBox="0 0 10 10"><rect x="2.5" y="0.5" width="5" height="3"/><rect x="0.5" y="3.5" width="9" height="4" rx="1"/><rect x="2.5" y="7" width="5" height="2.5"/></svg>030 714 263 592</div>
        <div class="row"><svg viewBox="0 0 10 10"><path d="M0.5 2h9v6h-9z M0.5 2l4.5 3.5L9.5 2" fill="var(--accent)"/></svg>info@sorgetaubewerden.example</div>
      </address>
    </header>

    <div class="return-line">SorgeTaubeWerden<span class="sep">|</span>Gustav-Lindner-Weg 7<span class="sep">|</span>10612 Berlin</div>
    <span class="fold-mark top"></span>
    <span class="fold-mark punch"></span>

    <div class="watermark" aria-hidden="true">SorgeTaubeWerden</div>

    <article class="letter">
      <div class="salutation">Herr Lindau</div>
      <p>Lorem ipsum dolor sit amet, consectetur adipiscing elit. Proin tincidunt, lectus id malesuada cursus, lorem augue egestas magna, ut mattis orci ante ut arcu. Sed mauris tellus, fermentum quis ligula nec, posuere pulvinar eros. Nam at mi quis velit pellentesque finibus. Donec lacus velit, faucibus mollis dolor nec, finibus pellentesque orci. Duis sed dictum elit, ut posuere arcu. Phasellus ac dolor et ante consequat rutrum nec nec tortor. Donec consequat, nibh sit amet pulvinar faucibus, turpis magna venenatis diam, vel pretium eros erat vestibulum nulla.</p>
      <p>Sed pretium ac enim eu viverra. Aliquam ac est eget magna convallis convallis. Aenean augue purus, finibus eget turpis quis, finibus dignissim nibh. Phasellus viverra lobortis dignissim. Duis varius turpis in sapien accumsan facilisis. Sed vehicula gravida diam a interdum. Nullam convallis ligula id erat egestas consequat. Integer consectetur ex vel aliquet iaculis. Vestibulum molestie sodales mauris, at tincidunt risus pellentesqu.</p>
      <p>Mauris facilisis, lectus at accumsan tincidunt, dui magna imperdiet sem, quis tempor est lectus eu ipsum. Praesent in fermentum nisl. Maecenas at lorem at odio interdum iaculis. Pellentesque cursus nulla nunc, ut suscipit nulla maximus et. Donec maximus rhoncus metus, vel laoreet nisi pretium sit amet. Donec posuere enim lectus, vitae aliquam augue tincidunt dignissim. Morbi vitae congue velit, quis elementum.</p>
      <div class="signature" role="img" aria-label="Handschriftliche Unterschrift"></div>
    </article>

    <footer>
      <div class="footer-info">
        <div class="col">Varen Bank AG München<br>Konto 00 584 392 71<br>BLZ 700 518 00</div>
        <div class="col">IBAN: DE47 7005 1800 0058 4392 7<br>BIC: VRKADEMMXXX</div>
        <div class="col">Sitz der Gesellschaft: Berlin, Deutschland<br>Geschäftsführung: Henrik Bosselt<br>Handelsregister: AG Berlin, HRB 258913</div>
        <div class="col">SteuerID 31/862/41597<br>IK Nummer 537 648 219</div>
      </div>
      <div class="footer-rule"></div>
      <div class="footer-band"></div>
      <div class="web-tab">www.sorgetaubewerden.example</div>
    </footer>
  </main>
</body>
</html>
```